TBNW site redesign

Please redesign a home page with content provided. PSD only - no coding
Can use any images from Vexelmarq.com

Please create a site design that more clearly illustrates the client's services and expertise. We are looking for a high-end design.

Any images used must be generic or of Dallas TX.

Fonts: Any
Colors: Match to logo
Look: Modern - Professional

Target Market(s)

medium-large business owners

Number of Pages Required

1 page

Font styles to use
Serif
Sans Serif

Requirements
Must have
• cohesive professional design
• high end look
• Match to logo

```html
<!DOCTYPE html>
<html lang="en">
<head>
<meta charset="utf-8">
<title>TBNW – Thornbury Commercial Realty Group</title>
<link rel="stylesheet" href="https://fonts.googleapis.com/css2?family=Montserrat:ital,wght@0,400;0,500;0,600;0,700;1,500&family=Open+Sans:ital,wght@0,400;0,600;1,400&display=swap">
<style>
:root{
  --red:#a50f14;
  --red-dark:#7d0b0f;
  --ink:#333333;
  --dark:#323232;
  --darker:#262626;
  --panel:#2a2a2a;
  --muted:#777777;
  --line:#d9d9d9;
  --white:#ffffff;
}
*{margin:0;padding:0;box-sizing:border-box}
html,body{width:1200px;height:4157px;overflow:hidden}
body{font-family:"Open Sans",Arial,sans-serif;color:var(--ink);background:var(--white);position:relative}
section,header,footer,nav{position:absolute;left:0;width:1200px}
.heading{font-family:"Montserrat",Arial,sans-serif;font-weight:600;font-size:38px;text-align:center;letter-spacing:1px}
.heading-rule{width:1000px;height:1px;margin:14px auto 0;background:var(--line);position:relative}
.heading-rule::after{content:"";position:absolute;left:450px;top:-1px;width:100px;height:3px;background:var(--red)}
.dark .heading{color:var(--white)}
.dark .heading-rule{background:#555}
.pill{display:inline-block;font-family:"Montserrat",Arial,sans-serif;font-weight:700;font-size:20px;letter-spacing:1px;border-radius:30px;text-transform:uppercase}

/* hero */
.hero{top:0;height:657px;background:linear-gradient(160deg,#0d1a2c 0%,#26384f 40%,#142236 70%,#0a1320 100%)}
.hero-photo{position:absolute;inset:0}
.brand{position:absolute;left:0;width:1200px;top:216px;text-align:center;color:var(--white);font-family:"Montserrat",Arial,sans-serif;font-weight:600}
.brand-mark{font-size:118px;line-height:190px;letter-spacing:6px}
.brand-name{font-size:44px;line-height:54px;letter-spacing:14px;margin-top:10px;text-transform:uppercase}
.brand-sub{font-size:28px;line-height:36px;letter-spacing:2px;margin-top:6px;text-transform:uppercase}

/* nav */
.main-nav{top:657px;height:63px;background:var(--red)}
.main-nav ul{list-style:none;position:absolute;left:83px;top:0;display:flex}
.main-nav li{font-family:"Montserrat",Arial,sans-serif;font-size:16px;color:var(--white);line-height:63px;margin-right:40px;position:relative}
.main-nav li.active::after{content:"";position:absolute;left:0;right:0;bottom:0;height:3px;background:var(--white)}
.nav-cta{position:absolute;left:956px;top:10px;width:166px;height:44px;border:2px solid var(--white);color:var(--white);text-align:center;line-height:40px;font-size:17px}

/* welcome */
.welcome{top:720px;height:416px;text-align:center}
.welcome .heading{margin-top:52px}
.welcome .lead{font-style:italic;font-size:18px;color:#555;margin-top:26px}
.welcome .body{width:880px;margin:14px auto 0;font-size:15px;line-height:28px;color:var(--muted)}
.welcome .pill{margin-top:24px;width:186px;height:52px;line-height:48px;border:2px solid var(--red);color:var(--red)}

/* why */
.why{top:1136px;height:521px;background:var(--dark)}
.why .heading{margin-top:42px}
.icon-box{position:absolute;width:111px;height:111px;border:3px solid var(--red);display:flex;align-items:center;justify-content:center}
.cross-v{position:absolute;left:599px;top:1386px;width:1px;height:100px;background:#555}
.cross-h{position:absolute;left:550px;top:1436px;width:100px;height:1px;background:#555}
.benefit{position:absolute;width:330px;color:var(--white)}
.benefit h3{font-family:"Montserrat",Arial,sans-serif;font-weight:500;font-size:22px;margin-bottom:12px}
.benefit p{font-size:14px;line-height:24px;color:#d5d5d5}
.benefit.left{text-align:right;left:80px}
.benefit.right{left:787px}

/* banner */
.banner{top:1657px;height:249px;background:linear-gradient(120deg,#8e0c11 0%,#b3161c 50%,#7a0a0e 100%);text-align:center;color:var(--white)}
.banner p{font-family:"Montserrat",Arial,sans-serif;font-style:italic;font-weight:500;font-size:26px;line-height:40px;margin-top:52px}
.banner .pill{margin-top:18px;width:270px;height:50px;line-height:50px;background:var(--white);color:var(--red);font-size:18px}

/* team */
.team{top:1906px;height:582px}
.team .heading{margin-top:54px}
.member{position:absolute;top:2045px;width:324px;height:360px;border:1px solid var(--line);text-align:center}
.member-photo{height:210px;margin-top:28px;background:linear-gradient(135deg,#b9a58a,#4d5560 50%,#1d2a44)}
.member h4{font-family:"Montserrat",Arial,sans-serif;font-weight:500;font-size:21px;margin-top:26px}
.member .rule{width:60px;height:2px;background:var(--red);margin:14px auto}
.member p{font-size:15px;color:var(--muted)}

/* testimonials */
.testimonials{top:2488px;height:452px;background:var(--dark)}
.testimonials .heading{margin-top:52px}
.quote{position:absolute;top:2677px;width:324px;height:185px;background:var(--panel);text-align:center;color:var(--white)}
.quote-badge{position:absolute;left:124px;top:-38px;width:76px;height:76px;border-radius:50%;background:var(--red);border:4px solid var(--white);display:flex;align-items:center;justify-content:center}
.quote p{font-size:14px;line-height:24px;padding:56px 30px 0}
.quote cite{display:block;font-style:normal;font-size:16px;margin-top:10px}

/* news */
.news{top:2940px;height:526px}
.news .heading{margin-top:52px}
.post{position:absolute;top:3090px;width:324px}
.post-photo{height:194px}
.post-date{position:absolute;top:219px;left:0;width:61px;height:83px;background:var(--red);color:var(--white);text-align:center;font-family:"Montserrat",Arial,sans-serif}
.post-date b{display:block;font-size:30px;font-weight:600;line-height:46px}
.post-date span{font-size:13px}
.post h5{position:absolute;left:84px;top:219px;font-size:15px;font-weight:600}
.post .excerpt{position:absolute;left:84px;top:248px;width:240px;font-size:14px;line-height:24px;color:var(--muted)}

/* signup */
.signup{top:3466px;height:109px;background:var(--red);color:var(--white)}
.signup p{position:absolute;left:78px;top:38px;font-family:"Montserrat",Arial,sans-serif;font-size:22px}
.signup .field{position:absolute;left:693px;top:33px;width:290px;height:42px;background:var(--red-dark);font-style:italic;font-size:14px;line-height:42px;padding-left:16px;color:#e7c5c6}
.signup b{position:absolute;left:1003px;top:40px;font-family:"Montserrat",Arial,sans-serif;font-size:19px;letter-spacing:1px}

/* footer */
.site-footer{top:3575px;height:393px;background:var(--dark);color:var(--white)}
.contact-card{position:absolute;left:78px;top:61px;width:304px;height:263px;border:1px solid #5a5a5a;padding:36px 22px}
.contact-card h6{font-family:"Montserrat",Arial,sans-serif;font-size:19px;font-weight:600;padding-bottom:14px;border-bottom:1px solid #5a5a5a}
.contact-row{display:flex;gap:14px;font-size:14px;line-height:24px;margin-top:20px;align-items:flex-start}
.contact-row svg{flex:none;margin-top:3px}
.quote-title{position:absolute;left:443px;top:52px;font-family:"Montserrat",Arial,sans-serif;font-weight:600;font-size:36px;letter-spacing:1px}
.quote-rule{position:absolute;left:443px;top:112px;width:680px;height:1px;background:#555}
.input{position:absolute;left:452px;width:274px;height:39px;background:var(--panel);font-style:italic;font-size:13px;color:#888;padding:10px 14px}
.input.msg{left:743px;top:163px;width:299px;height:141px}
.send{position:absolute;left:1058px;top:163px;width:64px;height:141px;background:var(--red);display:flex;align-items:center;justify-content:center}

.legal{top:3968px;height:189px;background:var(--darker);text-align:center;font-size:14px;color:#e6e6e6;padding-top:34px;line-height:33px}
.legal .link{color:var(--red)}
</style>
</head>
<body>

<header class="hero">
  <div class="hero-photo" role="img" aria-label="Upward view of glass office towers in downtown Dallas"></div>
  <div class="brand">
    <div class="brand-mark">TBNW</div>
    <div class="brand-name">Thornbury</div>
    <div class="brand-sub">Commercial Realty Group</div>
  </div>
</header>

<nav class="main-nav">
  <ul>
    <li class="active">HOME</li><li>SERVICES</li><li>ABOUT TBNW</li><li>MARKET NEWS</li><li>BLOG</li><li>CONTACT</li>
  </ul>
  <span class="pill nav-cta">Contact Us</span>
</nav>

<section class="welcome">
  <h1 class="heading">WELCOME TO TBNW</h1>
  <div class="heading-rule"></div>
  <p class="lead">Fast-track your search with tenant reps that only serve you, and specialize in the DFW area.</p>
  <p class="body">At TBNW, we focus solely on office and industrial/warehouse commercial real estate leasing and sales in the greater Dallas/Fort Worth area. We believe that our unique commercial office space service and market knowledge is the key to our clients' growth and ultimate business success. We strive to learn the specific needs of your company and be an essential team member that will find the best solution for your commercial real estate needs.</p>
  <span class="pill">Contact Us</span>
</section>

<section class="why dark">
  <h2 class="heading">WHY TENANT REPRESENTATION?</h2>
  <div class="heading-rule"></div>
</section>
<div class="cross-v"></div>
<div class="cross-h"></div>

<div class="benefit left" style="top:1288px"><h3>Relationships</h3><p>Save time by trusting TBNW year after year to find the right location for you.</p></div>
<div class="icon-box" style="left:457px;top:1291px"><svg width="56" height="50" viewBox="0 0 56 50"><path d="M28 46 6 24a13 13 0 0 1 22-17 13 13 0 0 1 22 17Z" fill="#fff"/><path d="M18 22l8 8 12-12" stroke="#323232" stroke-width="4" fill="none"/></svg></div>
<div class="icon-box" style="left:632px;top:1291px"><svg width="54" height="54" viewBox="0 0 54 54"><circle cx="27" cy="27" r="22" stroke="#fff" stroke-width="4" fill="none"/><text x="27" y="37" text-anchor="middle" font-family="Montserrat,sans-serif" font-size="28" font-weight="700" fill="#fff">$</text><path d="M10 10l34 34" stroke="#fff" stroke-width="4"/></svg></div>
<div class="benefit right" style="top:1288px"><h3>Free To You</h3><p>You pay us nothing. We get our commission from the property being leased.</p></div>

<div class="benefit left" style="top:1468px"><h3>Access to More</h3><p>We have no agreements or personal incentives for specific properties.</p></div>
<div class="icon-box" style="left:457px;top:1471px"><svg width="60" height="40" viewBox="0 0 60 40"><path d="M2 30h14l10 6h18l14-10-4-4-12 6H30" stroke="#fff" stroke-width="4" fill="none"/><circle cx="40" cy="12" r="10" fill="#fff"/></svg></div>
<div class="icon-box" style="left:632px;top:1471px"><svg width="56" height="54" viewBox="0 0 56 54"><circle cx="28" cy="12" r="9" fill="#fff"/><path d="M14 36c0-8 6-13 14-13s14 5 14 13Z" fill="#fff"/><path d="M2 44h16l8 6h22l6-6" stroke="#fff" stroke-width="4" fill="none"/></svg></div>
<div class="benefit right" style="top:1468px"><h3>Customized Service</h3><p>Aside from saving you the time of repeating what your needs are to each new location.</p></div>

<section class="banner" role="img" aria-label="Red-tinted view of office towers behind a call to action">
  <p>If you need to find office or warehouse space in the Dallas Fort Worth<br>area, the team at TBNW has the experience you need.</p>
  <span class="pill">Space Calculator</span>
</section>

<section class="team">
  <h2 class="heading">MEET THE TEAM</h2>
  <div class="heading-rule"></div>
</section>
<div class="member" style="left:78px"><div class="member-photo" role="img" aria-label="Portrait of the founder in a suit in an office"></div><h4>Evan R. Thornbury</h4><div class="rule"></div><p>Founder and President</p></div>
<div class="member" style="left:438px"><div class="member-photo" role="img" aria-label="Portrait of the senior director in a suit in an office"></div><h4>Owen Castell-Reid</h4><div class="rule"></div><p>Senior Director</p></div>
<div class="member" style="left:798px"><div class="member-photo" role="img" aria-label="Portrait of the junior associate in a suit in an office"></div><h4>Daniel Ross Avery</h4><div class="rule"></div><p>Jr. Associate</p></div>

<section class="testimonials dark">
  <h2 class="heading">WHAT OUR CLIENT SAY</h2>
  <div class="heading-rule"></div>
</section>
<div class="quote" style="left:78px"><div class="quote-badge"><svg width="30" height="26" viewBox="0 0 30 26"><path d="M2 2h11v11l-5 11H3l4-11H2Zm15 0h11v11l-5 11h-5l4-11h-5Z" fill="#fff"/></svg></div><p>Lorem Ipsum is simply dummy text of the printing and typesetting industry. Lorem Ipsum has been the industry.</p><cite>-Commentetor Name</cite></div>
<div class="quote" style="left:438px"><div class="quote-badge"><svg width="30" height="26" viewBox="0 0 30 26"><path d="M2 2h11v11l-5 11H3l4-11H2Zm15 0h11v11l-5 11h-5l4-11h-5Z" fill="#fff"/></svg></div><p>Lorem Ipsum is simply dummy text of the printing and typesetting industry. Lorem Ipsum has been the industry.</p><cite>-Commentetor Name</cite></div>
<div class="quote" style="left:798px"><div class="quote-badge"><svg width="30" height="26" viewBox="0 0 30 26"><path d="M2 2h11v11l-5 11H3l4-11H2Zm15 0h11v11l-5 11h-5l4-11h-5Z" fill="#fff"/></svg></div><p>Lorem Ipsum is simply dummy text of the printing and typesetting industry. Lorem Ipsum has been the industry.</p><cite>-Commentetor Name</cite></div>

<section class="news">
  <h2 class="heading">LATEST NEWS</h2>
  <div class="heading-rule"></div>
</section>
<article class="post" style="left:78px"><div class="post-photo" role="img" aria-label="Business team meeting around a table" style="background:linear-gradient(135deg,#d9d2c8,#8a8178 50%,#3e3a36)"></div><div class="post-date"><b>29</b><span>APR</span></div><h5>Lorem Ipsum is simply dummy.</h5><p class="excerpt">Lorem Ipsum is simply dummy text of the printing and typesetting.</p></article>
<article class="post" style="left:438px"><div class="post-photo" role="img" aria-label="Hands working on a laptop with glowing light" style="background:linear-gradient(135deg,#2c2622,#8a5a33 50%,#e3c9a3)"></div><div class="post-date"><b>29</b><span>APR</span></div><h5>Lorem Ipsum is simply dummy.</h5><p class="excerpt">Lorem Ipsum is simply dummy text of the printing and typesetting.</p></article>
<article class="post" style="left:798px"><div class="post-photo" role="img" aria-label="Businessman looking up at sunlit office towers" style="background:linear-gradient(135deg,#4a6f9a,#b8cde0 50%,#f6f3ea)"></div><div class="post-date"><b>29</b><span>APR</span></div><h5>Lorem Ipsum is simply dummy.</h5><p class="excerpt">Lorem Ipsum is simply dummy text of the printing and typesetting.</p></article>

<section class="signup">
  <p>To get latest updates and promotions signup now!</p>
  <div class="field">Enter Your Email</div>
  <b>SUBSCRIBE</b>
</section>

<footer class="site-footer">
  <div class="contact-card">
    <h6>CONTACT DETAIL</h6>
    <div class="contact-row"><svg width="16" height="22" viewBox="0 0 16 22"><path d="M8 0a8 8 0 0 0-8 8c0 6 8 14 8 14s8-8 8-14a8 8 0 0 0-8-8Zm0 11a3 3 0 1 1 0-6 3 3 0 0 1 0 6Z" fill="#a50f14"/></svg><span>1420 Cedar Vale Avenue, Suite 610, Dallas, TX 75201</span></div>
    <div class="contact-row"><svg width="18" height="18" viewBox="0 0 18 18"><path d="M4 1l3 4-2 2c1 2 3 4 5 5l2-2 4 3-2 4C7 17 1 11 0 5Z" fill="#a50f14"/></svg><span>214-555-0148</span></div>
    <div class="contact-row"><svg width="18" height="18" viewBox="0 0 18 18"><rect x="2" y="1" width="14" height="16" rx="2" fill="#a50f14"/><rect x="5" y="4" width="8" height="4" fill="#323232"/></svg><span>214-555-0192</span></div>
  </div>
  <div class="quote-title">REQUEST A FREE QUOTE</div>
  <div class="quote-rule"></div>
  <div class="input" style="top:163px">Name</div>
  <div class="input" style="top:214px">Email</div>
  <div class="input" style="top:265px">Phone</div>
  <div class="input msg">Message</div>
  <div class="send"><svg width="26" height="26" viewBox="0 0 26 26"><path d="M1 12 25 1 16 25l-4-9Z" fill="#fff"/></svg></div>
</footer>

<footer class="legal">
  <p>State Real Estate Commission Mandated Disclosure Notices – click links below to view pages</p>
  <p class="link">Information About Brokerage Services · Consumer Notice</p>
  <p class="link">Consumer Protection Notice · Agency Disclosure</p>
  <p>2018 ©THORNBURY COMMERCIAL REALTY GROUP . All Rights Reserved.</p>
</footer>

</body>
</html>
```